Medical clinic VALORENT sales materials presentation folder

I am looking for a professional design to a sales/presentation folder for VALORENT medical clinic. I would like to get picture of doctor in a class design.
I had an example of a hold marketing and the VALORENT LOGO.
VALORENT have 5 clinics and we are serious whit lot of doctors. We are doing lot of medical service. I put a doctor picture, but if you have a better choice for the presentation folder don't hesitate to use it.

Target Market(s)

Medical customer and corporation

Industry/Entity Type

Health care

Requirements
Must have
• Professional design - red accent
Nice to have
• Medical doctor picture
Should not have
• Don't want the same hold design that the example

```html
<!DOCTYPE html>
<html lang="fr">
<head>
<meta charset="utf-8">
<title>VALORENT – Pochette de présentation</title>
<link rel="stylesheet" href="https://fonts.googleapis.com/css2?family=Open+Sans:wght@600;700;800&display=swap">
<style>
  :root {
    --folder-red: #c0232f;
    --accent-red: #d9202c;
    --band-red: #e01f2d;
    --deep-red: #b30000;
    --pocket-dark: #2a2a2a;
    --panel-grey: #efefef;
    --ink: #2b2b2b;
    --brand-brown: #3e2a1f;
    --cross-orange: #ee7f57;
    --soft-pink: #e8cfd2;
    --white: #ffffff;
  }
  * { margin: 0; padding: 0; box-sizing: border-box; }
  html, body {
    width: 1200px; height: 1042px; overflow: hidden; background: var(--white);
  }
  .folder-sheet {
    position: relative; width: 1200px; height: 1042px;
    font-family: "Open Sans", Arial, sans-serif;
  }
  .folder-shapes { position: absolute; inset: 0; }
  .cover-brand {
    position: absolute; left: 71px; width: 553px; top: 356px;
    display: flex; align-items: center; justify-content: center; gap: 12px;
    color: var(--white); font-weight: 800; font-size: 28px; letter-spacing: 1px;
  }
  .cover-brand .brand-square {
    width: 30px; height: 30px; background: var(--white);
  }
  .inside-brand {
    position: absolute; left: 685px; top: 30px;
    display: flex; align-items: center; gap: 12px;
    color: var(--brand-brown); font-weight: 800; font-size: 22px; letter-spacing: 1px;
  }
  .inside-brand .brand-square {
    width: 34px; height: 34px; background: var(--accent-red);
  }
  .headline {
    position: absolute; left: 667px; top: 108px;
    color: var(--accent-red); font-weight: 700; font-size: 42px;
    line-height: 33px; letter-spacing: 2px;
  }
  .intro {
    position: absolute; left: 667px; top: 190px; width: 460px;
    color: var(--ink); font-weight: 700; font-size: 12.6px;
    line-height: 17.5px; letter-spacing: 1px; text-align: justify;
    hyphens: manual;
  }
  .clinics-title {
    position: absolute; left: 667px; top: 283px;
    display: flex; align-items: flex-start;
    color: var(--accent-red); font-weight: 700; font-size: 19.5px;
    line-height: 26px; letter-spacing: 1.1px; white-space: nowrap;
  }
  .clinics-title .title-cross {
    width: 29px; height: 29px; margin-left: 4px; margin-top: 2px; flex: none;
  }
  .clinic-list { position: absolute; left: 709px; top: 306px; list-style: none; }
  .clinic-list li {
    position: relative; padding-left: 22px; height: 27.4px;
    color: var(--ink); font-weight: 700; font-size: 15.5px; letter-spacing: 1.3px; line-height: 22px;
  }
  .clinic-list li::before, .clinic-list li::after {
    content: ""; position: absolute; background: var(--accent-red);
  }
  .clinic-list li::before { left: 0; top: 8px; width: 18px; height: 6px; }
  .clinic-list li::after { left: 6px; top: 2px; width: 6px; height: 18px; }
  .contact-list { position: absolute; left: 667px; top: 676px; list-style: none; }
  .contact-list li {
    display: flex; align-items: center; gap: 8px; height: 28px;
    color: var(--ink); font-weight: 600; font-size: 11px; letter-spacing: 0.9px;
  }
  .contact-list svg { width: 21px; height: 21px; flex: none; }
  .doctor-photo {
    position: absolute; left: 906px; top: 344px; width: 240px; height: 435px;
    border-radius: 110px 110px 0 0;
    background: linear-gradient(180deg, #d9d2cf 0%, #f4f4f4 45%, #e6e6ea 100%);
  }
</style>
</head>
<body>
<div class="folder-sheet">
  <svg class="folder-shapes" width="1200" height="1042" viewBox="0 0 1200 1042" aria-hidden="true">
    <defs>
      <linearGradient id="blush-band" x1="0" y1="0" x2="1" y2="0">
        <stop offset="0" stop-color="#e57784"/>
        <stop offset="0.6" stop-color="#e8808a"/>
        <stop offset="1" stop-color="#f0987b"/>
      </linearGradient>
      <linearGradient id="grey-swoosh" x1="0" y1="0" x2="0" y2="1">
        <stop offset="0" stop-color="#efefef"/>
        <stop offset="1" stop-color="#d4d4d4"/>
      </linearGradient>
      <pattern id="white-dots" width="7" height="7" patternUnits="userSpaceOnUse">
        <circle cx="2" cy="2" r="1.1" fill="#ffffff"/>
      </pattern>
      <pattern id="red-dots" width="21" height="21" patternUnits="userSpaceOnUse">
        <circle cx="5" cy="5" r="2.6" fill="#e01f2d"/>
      </pattern>
    </defs>

    <rect class="cover-panel" x="71" y="8" width="553" height="771" fill="var(--folder-red)"/>
    <polygon class="side-flap" points="8,553 58,536 58,776 34,776 8,761" fill="var(--pocket-dark)"/>
    <polygon class="pocket-flap" points="73,792 593,792 542,1035 73,1036" fill="var(--pocket-dark)"/>

    <rect class="inside-panel" x="639" y="8" width="555" height="771" fill="var(--panel-grey)"/>
    <path class="grey-swoosh" d="M639,420 Q700,380 760,400 Q790,470 760,530 Q720,585 639,592 Z" fill="url(#grey-swoosh)"/>
    <path class="light-wedge" d="M1010,8 L1194,8 L1194,190 Q1150,150 1120,110 Z" fill="#e6e6e6" opacity="0.6"/>
    <path class="blush-band" d="M639,8 L915,8 L915,45 Q912,110 840,105 Q740,95 639,74 Z" fill="url(#blush-band)"/>

    <path class="faint-cross" d="M1113,8 L1194,8 L1194,94 L1161,94 L1161,47 L1113,47 Z" fill="var(--soft-pink)" opacity="0.8"/>
    <path class="faint-cross" d="M1171,254 L1194,254 L1194,395 L1171,395 L1171,348 L1123,348 L1123,301 L1171,301 Z" fill="var(--soft-pink)" opacity="0.8"/>
    <rect x="1141" y="298" width="53" height="53" fill="url(#red-dots)"/>
    <circle class="ring" cx="1156" cy="187" r="12" fill="none" stroke="#e8604f" stroke-width="3"/>

    <path class="red-band" d="M885,779 L830,705 Q790,650 800,600 Q815,520 900,480 Q930,468 960,466 L1194,436 L1194,779 Z" fill="var(--band-red)"/>
    <path class="band-line" d="M932,757 L890,680 Q860,625 885,580 Q905,555 940,548" fill="none" stroke="#ffffff" stroke-width="1.6"/>
    <line class="band-line" x1="1095" y1="495" x2="1194" y2="466" stroke="#ffffff" stroke-width="1.6"/>
    <rect x="852" y="517" width="30" height="52" fill="url(#white-dots)"/>
    <rect x="1165" y="505" width="28" height="30" fill="url(#white-dots)"/>
    <path class="white-cross" d="M827,574 h8 v7 h7 v8 h-7 v7 h-8 v-7 h-7 v-8 h7 z" fill="#ffffff"/>
    <path class="corner-cross" d="M1159,724 h19 v19 h16 v19 h-16 v17 h-19 v-17 h-20 v-19 h20 z" fill="var(--deep-red)"/>
  </svg>

  <div class="cover-brand"><span class="brand-square"></span>VALORENT</div>

  <div class="inside-brand"><span class="brand-square"></span>VALORENT</div>

  <h1 class="headline">VOTRE SANTÉ EST<br>NOTRE PRIORITÉ</h1>

  <p class="intro">VALORENT DIAGNOSTIC EFFECTUE LA VENTE, LA FABRICATION / PRODUCTION D'APPAREIL MÉDICAL DE CLASS1 ET LA DISTRIBU&shy;TION D'APPAREIL MÉDICAUX. ELLE SE SPÉCIALISE DANS LES KITS DE TEST POUR LABORATOIRE.</p>

  <h2 class="clinics-title">NOUS AVONS CINQ CLINIQUES<svg class="title-cross" viewBox="0 0 29 29" aria-hidden="true"><path d="M10,0 h9 v10 h10 v9 h-10 v10 h-9 v-10 h-10 v-9 h10 z" fill="var(--cross-orange)"/></svg></h2>
  <ul class="clinic-list">
    <li>GATINEAU</li>
    <li>GASPE</li>
    <li>LEVIS</li>
    <li>MONTREAL</li>
    <li>QUEBEC</li>
    <li>SHERBROOKE</li>
  </ul>

  <div class="doctor-photo" role="img" aria-label="Photo d'une médecin en blouse blanche avec stéthoscope"></div>

  <ul class="contact-list">
    <li>
      <svg viewBox="0 0 22 22" aria-hidden="true"><circle cx="11" cy="11" r="10" fill="#d9202c"/><g fill="none" stroke="#fff" stroke-width="1.2"><circle cx="11" cy="11" r="6.5"/><ellipse cx="11" cy="11" rx="3" ry="6.5"/><line x1="4.5" y1="11" x2="17.5" y2="11"/><line x1="11" y1="4.5" x2="11" y2="17.5"/></g></svg>
      www.valorent.ca/
    </li>
    <li>
      <svg viewBox="0 0 22 22" aria-hidden="true"><circle cx="11" cy="11" r="10" fill="none" stroke="#d9202c" stroke-width="1.3"/><path d="M7.5,6 l2,-0.5 l1.3,2.8 l-1.3,1 q0.9,2 2.6,3 l1,-1.2 l2.8,1.3 l-0.5,2 q-5.5,0.5 -7.9,-8.4 z" fill="#d9202c"/></svg>
      418 555-0148
    </li>
    <li>
      <svg viewBox="0 0 22 22" aria-hidden="true"><circle cx="11" cy="11" r="10" fill="none" stroke="#d9202c" stroke-width="1.3"/><rect x="5.5" y="7.5" width="11" height="7.5" fill="#d9202c"/><path d="M5.5,7.5 L11,11.8 L16.5,7.5" fill="none" stroke="#fff" stroke-width="1"/></svg>
      info@valorentmed.com
    </li>
  </ul>
</div>
</body>
</html>
```